Business Card Design Project

Recently had a new logo made up for my company and new business cards done as well. I have attached the logos for your viewing. Additional projects may be needed. Good luck!

Industry/Entity Type

Business

```html
<!DOCTYPE html>
<html lang="en">
<head>
<meta charset="utf-8">
<title>Marlow Financial Group — Business Card</title>
<link rel="stylesheet" href="https://fonts.googleapis.com/css2?family=Crimson+Pro:wght@400;500&family=Arimo:wght@400&display=swap">
<style>
  :root {
    --card-bg: #23242d;
    --panel-faint: #2b2c33;
    --gold: #cdb88a;
    --rule: #8b7b5b;
    --white: #ffffff;
  }
  html, body {
    margin: 0;
    padding: 0;
    width: 1200px;
    height: 686px;
    overflow: hidden;
    background: var(--card-bg);
  }
  .card {
    position: relative;
    width: 1200px;
    height: 686px;
    background: var(--card-bg);
    font-family: "Crimson Pro", Georgia, serif;
  }
  .faint-panel {
    position: absolute;
    left: 581px;
    top: 34px;
    width: 565px;
    height: 606px;
    background: var(--panel-faint);
  }
  .brand {
    position: absolute;
    left: 130px;
    top: 168px;
    width: 300px;
    text-align: center;
    color: var(--gold);
    font-family: "Crimson Pro", Georgia, serif;
    font-weight: 500;
  }
  .brand-square {
    display: block;
    width: 150px;
    height: 150px;
    margin: 0 auto 34px;
    background: var(--gold);
  }
  .brand-name {
    margin: 0;
    font-size: 62px;
    line-height: 1;
    letter-spacing: 3px;
    text-transform: uppercase;
  }
  .brand-sub {
    margin: 8px 0 0;
    font-size: 26px;
    line-height: 1;
    letter-spacing: 3px;
    text-transform: uppercase;
  }
  .divider {
    position: absolute;
    left: 523px;
    top: 95px;
    width: 4px;
    height: 498px;
    background: var(--rule);
  }
  .contact {
    position: absolute;
    left: 629px;
    top: 168px;
  }
  .person-name {
    margin: 0;
    font-family: "Crimson Pro", Georgia, serif;
    font-weight: 400;
    font-size: 56px;
    line-height: 1;
    color: var(--gold);
  }
  .person-title {
    margin: 6px 0 0;
    font-family: "Arimo", Arial, sans-serif;
    font-size: 25px;
    line-height: 1.2;
    color: var(--white);
  }
  .details {
    list-style: none;
    margin: 50px 0 0;
    padding: 0;
    font-size: 22px;
    color: var(--gold);
    letter-spacing: 0.3px;
  }
  .details li {
    height: 43px;
    line-height: 43px;
  }
</style>
</head>
<body>
  <main class="card">
    <div class="faint-panel" aria-hidden="true"></div>

    <div class="brand">
      <span class="brand-square" aria-hidden="true"></span>
      <p class="brand-name">Marlow</p>
      <p class="brand-sub">Financial Group</p>
    </div>

    <div class="divider" aria-hidden="true"></div>

    <section class="contact">
      <h1 class="person-name">Daniel R. Marlow</h1>
      <p class="person-title">Estate Planning and Insurance Specialist</p>
      <ul class="details">
        <li>P: 555-0142-7310 | F: 555-0142-7311</li>
        <li>4100 Harbor Valley Road, Suite 310E,</li>
        <li>Eastbrook, New York 11700</li>
        <li>Dmarlow@marlowfinancial.com</li>
        <li>www.marlowfinancial.com</li>
      </ul>
    </section>
  </main>
</body>
</html>
```